Corvane Communications ISP Flyer

Our company is Corvane Communications. We need to create a flyer to market our Internet/Phone services to a retirement community. We will be offering 50x50 internet connection along with a single phone line for $49.99 (before taxes). We would like to emphasize that our services are over fiber optic cables.

Internet Service
- 50x50 megabit fiber internet connection
- up to 5 email addresses
- 10gb of online storage

Phone Service
- Local 956 Phone number
- Unlimited Local/Long distance
- Caller Id
- Web access to Voicemail

Target Market(s)

Residential Customers

Industry/Entity Type

Internet

Requirements
Must have
• Company Name - Corvane Communications
Service detail

Contact info -

sales@corvaneco.example
956-483-2619

```html
<!DOCTYPE html>
<html lang="en">
<head>
<meta charset="utf-8">
<title>Corvane Communications – Internet &amp; Phone Flyer</title>
<link rel="stylesheet" href="https://fonts.googleapis.com/css2?family=Alfa+Slab+One&family=Open+Sans:wght@700;800&display=swap">
<style>
  :root {
    --bg: #000000;
    --white: #ffffff;
    --grey-text: #b4b4b4;
    --accent: #3b8fd4;
    --rule: #2f7fc4;
    --divider-light: #d6d6d6;
    --divider-dark: #8c8c8c;
    --deep-blue: #0a2a5a;
    --mid-blue: #1f6fc0;
    --glow-blue: #4fb0ff;
  }
  html, body {
    margin: 0;
    padding: 0;
    overflow: hidden;
    background: var(--bg);
  }
  .flyer {
    position: relative;
    width: 1000px;
    height: 1200px;
    overflow: hidden;
    background: var(--bg);
    font-family: "Open Sans", Arial, sans-serif;
    color: var(--white);
  }
  .side-art {
    position: absolute;
    left: 0; top: 0;
    width: 216px; height: 1200px;
    background:
      linear-gradient(160deg, rgba(120,190,255,0.55) 0%, rgba(20,70,140,0) 35%),
      linear-gradient(200deg, var(--deep-blue) 0%, var(--mid-blue) 45%, #0d3d7a 70%, #5aaef0 100%);
  }
  .side-divider {
    position: absolute;
    left: 216px; top: 0;
    width: 20px; height: 1200px;
    background: linear-gradient(90deg, var(--divider-dark), var(--divider-light) 40%, var(--divider-dark));
  }
  .fiber-glow {
    position: absolute;
    left: 640px; top: 820px;
    width: 360px; height: 380px;
    background: radial-gradient(ellipse at 75% 80%, rgba(120,200,255,0.85) 0%, rgba(40,120,220,0.55) 30%, rgba(10,40,100,0.25) 60%, rgba(0,0,0,0) 80%);
  }
  .title {
    position: absolute;
    left: 250px; top: 42px;
    width: 724px;
    margin: 0;
    font-family: "Alfa Slab One", Georgia, serif;
    font-weight: 400;
    font-size: 40px;
    line-height: 1;
    text-align: center;
    letter-spacing: 0.5px;
  }
  .rule {
    position: absolute;
    height: 3px;
    background: var(--rule);
  }
  .rule--title { left: 250px; top: 116px; width: 724px; }
  .rule--fiber { left: 274px; top: 896px; width: 666px; }
  .section-heading {
    position: absolute;
    margin: 0;
    font-family: "Alfa Slab One", Georgia, serif;
    font-weight: 400;
    font-size: 44px;
    line-height: 1;
  }
  .section-heading--internet { left: 262px; top: 180px; }
  .section-heading--phone { left: 268px; top: 404px; }
  .feature-list {
    position: absolute;
    margin: 0;
    padding: 0;
    list-style: none;
    color: var(--grey-text);
    font-weight: 800;
    font-size: 25px;
  }
  .feature-list li { height: 42px; line-height: 42px; }
  .feature-list li::before { content: "- "; }
  .feature-list--internet { left: 262px; top: 244px; }
  .feature-list--phone { left: 266px; top: 466px; }
  .offer {
    position: absolute;
    left: 276px; top: 670px;
    margin: 0;
    color: var(--accent);
    font-weight: 800;
    font-size: 26px;
    line-height: 42px;
  }
  .offer .price { color: var(--white); }
  .fiber-note {
    position: absolute;
    left: 284px; top: 848px;
    margin: 0;
    font-weight: 800;
    font-size: 26px;
    line-height: 1;
  }
  .contact {
    position: absolute;
    margin: 0;
    font-weight: 800;
    font-size: 33px;
    line-height: 1;
  }
  .contact--email { left: 284px; top: 984px; }
  .contact--phone { left: 350px; top: 1050px; display: flex; align-items: center; gap: 22px; }
  .contact-icon {
    width: 50px; height: 52px;
    border-radius: 8px;
    background: var(--glow-blue);
    display: flex; align-items: center; justify-content: center;
  }
</style>
</head>
<body>
<div class="flyer">
  <div class="side-art" role="img" aria-label="Abstract blue glass blocks illustration"></div>
  <div class="side-divider"></div>
  <div class="fiber-glow" role="img" aria-label="Glowing blue fiber optic strands"></div>

  <h1 class="title">Corvane Communications</h1>
  <div class="rule rule--title"></div>

  <h2 class="section-heading section-heading--internet">Internet Service</h2>
  <ul class="feature-list feature-list--internet">
    <li>50x50 megabit fiber internet connection</li>
    <li>up to 5 email addresses</li>
    <li>10gb of online storage</li>
  </ul>

  <h2 class="section-heading section-heading--phone">Phone Service</h2>
  <ul class="feature-list feature-list--phone">
    <li>Local 956 Phone number</li>
    <li>Unlimited Local/Long distance</li>
    <li>Caller Id</li>
    <li>Web access to Voicemail</li>
  </ul>

  <p class="offer">50x50 internet connection<br>along with a single phone line<br>for <span class="price">$49.99</span> (before taxes)</p>

  <p class="fiber-note">Our services are over fiber optic cables</p>
  <div class="rule rule--fiber"></div>

  <p class="contact contact--email">sales@corvaneco.example</p>
  <p class="contact contact--phone">
    <span class="contact-icon">
      <svg width="30" height="30" viewBox="0 0 24 24" aria-hidden="true">
        <path fill="#ffffff" d="M6.6 10.8a15.1 15.1 0 0 0 6.6 6.6l2.2-2.2a1 1 0 0 1 1-.25 11.4 11.4 0 0 0 3.6.57 1 1 0 0 1 1 1V20a1 1 0 0 1-1 1A17 17 0 0 1 3 4a1 1 0 0 1 1-1h3.5a1 1 0 0 1 1 1c0 1.25.2 2.45.57 3.57a1 1 0 0 1-.25 1z"/>
      </svg>
    </span>
    956-483-2619
  </p>
</div>
</body>
</html>
```